Letterhead Design Project

Attached is our new Logo and a copy of our old letter head
Looking to rebrand with our new logo

Reason: I want to show a business card design

Industry/Entity Type

Film Production

Colors

Designer to choose colors to be used in the design.

Requirements
Must have
• The information on the old letterhead

```html
<!DOCTYPE html>
<html lang="en">
<head>
<meta charset="utf-8">
<title>KORVA International Letterhead</title>
<link rel="stylesheet" href="https://fonts.googleapis.com/css2?family=Josefin+Sans:wght@700&family=Raleway:wght@400&display=swap">
<style>
  :root {
    --sky: #b3e1f2;
    --navy: #0a4a6e;
    --ocean: #0277ab;
    --rust: #e5612a;
    --paper: #ffffff;
    --ink: #0b4769;
  }
  * { margin: 0; padding: 0; box-sizing: border-box; }
  html, body { width: 927px; height: 1200px; overflow: hidden; background: var(--paper); }
  .letterhead { position: relative; width: 927px; height: 1200px; overflow: hidden; background: var(--paper); }
  .artwork { position: absolute; left: 0; display: block; }
  .artwork--top { top: 0; }
  .artwork--bottom { bottom: 0; }
  .brand {
    position: absolute; right: 26px; top: 50px;
    display: flex; align-items: center; gap: 10px;
    font-family: "Josefin Sans", sans-serif; font-weight: 700; color: var(--ocean);
  }
  .brand__dot { width: 22px; height: 22px; border-radius: 50%; background: var(--ocean); }
  .brand__name { display: flex; flex-direction: column; align-items: flex-end; line-height: 1; }
  .brand__word { font-size: 54px; letter-spacing: 1px; }
  .brand__sub { font-size: 16px; letter-spacing: 3.2px; margin-top: 6px; }
  .header-info { position: absolute; right: 26px; top: 168px; text-align: right; }
  .tagline {
    font-family: "Josefin Sans", sans-serif; font-weight: 700; font-size: 19px;
    color: var(--rust); line-height: 1;
  }
  .contact {
    font-family: "Raleway", sans-serif; font-weight: 400; font-size: 19.5px;
    color: var(--ink); line-height: 24px; margin-top: 5px;
  }
  .contact__line--center { padding-right: 34px; }
  .footer { position: absolute; left: 0; right: 0; top: 1126px; text-align: center; color: var(--ink); }
  .divisions { font-family: "Josefin Sans", sans-serif; font-weight: 700; font-size: 16.5px; line-height: 1; }
  .legal { font-family: "Raleway", sans-serif; font-size: 15px; line-height: 18px; margin-top: 2px; }
</style>
</head>
<body>
<main class="letterhead">
  <svg class="artwork artwork--top" width="927" height="400" viewBox="0 0 927 400" role="img" aria-label="Decorative sweeping blue and orange corner artwork">
    <defs>
      <linearGradient id="corner-tone" x1="0" y1="0.2" x2="1" y2="0">
        <stop offset="0" stop-color="#b3e1f2"/>
        <stop offset="0.45" stop-color="#5fb4d8"/>
        <stop offset="1" stop-color="#0277ab"/>
      </linearGradient>
    </defs>
    <path d="M0,0 L927,0 L927,6 C560,50 220,170 0,388 Z" fill="url(#corner-tone)"/>
  </svg>

  <div class="brand">
    <span class="brand__dot"></span>
    <span class="brand__name">
      <span class="brand__word">KORVA</span>
      <span class="brand__sub">INTERNATIONAL</span>
    </span>
  </div>

  <header class="header-info">
    <p class="tagline">SUPPLY &amp; MANAGEMENT OF INFRASTRUCTURE &amp; LOGISTICS</p>
    <div class="contact">
      <p class="contact__line">P.O. Box 482 Fernvale QLD 4306&nbsp;&nbsp;&nbsp;P.O.Box 719 Lurnea NSW 2171</p>
      <p class="contact__line contact__line--center">Phone no.: 0400 555 018 | Email add.: hello@korva.com.au</p>
    </div>
  </header>

  <svg class="artwork artwork--bottom" width="927" height="250" viewBox="0 0 927 250" role="img" aria-label="Decorative sweeping blue and orange footer artwork">
    <defs>
      <linearGradient id="footer-tone" x1="0" y1="0" x2="1" y2="0">
        <stop offset="0" stop-color="#b3e1f2"/>
        <stop offset="0.6" stop-color="#b3e1f2"/>
        <stop offset="1" stop-color="#7fc6e4"/>
      </linearGradient>
    </defs>
    <path d="M0,122 C260,160 600,170 927,0 L927,250 L0,250 Z" fill="url(#footer-tone)"/>
  </svg>

  <footer class="footer">
    <p class="divisions">KORVA FILM SERVICES | KORVA PILOT ESCORTS | KORVA TOUR MANAGEMENT | KORVA DRIVER</p>
    <p class="legal">are divisions of KORVA International Pty Ltd</p>
    <p class="legal">ACN 000 111 222&nbsp;&nbsp;ABN 00 000 111 222</p>
  </footer>
</main>
</body>
</html>
```